New Web Design Project- Maplebrook Elders

Maplebrook Elders is the Capital regions premiere, non-medical, in-home care & companionship service that unites "junior-senior" caregivers with "senior-senior" care recipients so that senior-seniors can remain safe & independent in their own homes.
Our compassionate "junior-senior" caregivers are all retirees that have already enjoyed rewarding careers and/or have raised families of their own and feel the need to pay-it-forward with their care for older seniors.
Services include grocery shopping, medical or dental appointments, errands, meal preparation & cleanup, light housekeeping, bed making, laundry, hobbies, reading, transportation, entertainment, games, mobility assistance/transfers, respite care, light yard work, pet walking.

Target Market(s)

Grown children of senior-seniors between who are between 55-70, predominantly the daughters (female). End users of services (senior-seniors) are typically 80-100 years old and living in own homes

Industry/Entity Type

Medical

Coding

Coded - Design and coding required

Number of Pages Required

5+ page

Font styles to use
Sans Serif

Colors
3277b5
ec1f27

Requirements
Must have
• supporting photos on each page. Contact us page. Promotional video (done) attached that doesn't take viewers off my site (https://vidshare.example/Kq7PzLm2Wx4).
• Also, need my downloadable brochure (attached).
• The following pages:
• Home. Services. About Us. News. Employment. Contact us. Junior-Seniors Assisting Senior-Seniors. Why non-medical in-home care. Who are junior-seniors?Financial effects of senior care. Do you need care? Does someone you love need care?
Should not have
• Any other photos or images other than what I've supplied.

```html
<!DOCTYPE html>
<html lang="en">
<head>
<meta charset="utf-8">
<title>Maplebrook Elders – Home</title>
<link rel="stylesheet" href="https://fonts.googleapis.com/css2?family=Noto+Serif:wght@400;700&family=Open+Sans:wght@400;600;700&display=swap">
<style>
:root{
  --blue:#3277b5;
  --blue-dark:#23558f;
  --red:#ec1f27;
  --red-dark:#c4121a;
  --ink:#222;
  --muted:#666;
  --line:#d7d7d7;
  --white:#fff;
}
*{box-sizing:border-box;margin:0;padding:0}
html,body{width:1200px;height:3005px;overflow:hidden;background:var(--white)}
body{position:relative;font-family:"Open Sans",Arial,sans-serif;color:var(--ink)}

/* header */
.site-header{position:absolute;left:0;top:0;width:1200px;height:120px;background:linear-gradient(#fff,#f1f1f1)}
.brand{position:absolute;left:100px;top:30px;display:flex;align-items:center;gap:10px;font-family:"Noto Serif",Georgia,serif;font-size:22px;color:var(--blue-dark)}
.brand-mark{width:24px;height:24px;background:var(--blue)}
.contact-bar{position:absolute;top:12px;left:478px;display:flex;align-items:center;font-size:14px;color:var(--ink)}
.contact-bar .ico{width:32px;height:32px;border-radius:50%;display:flex;align-items:center;justify-content:center;margin-right:10px}
.ico.dark{background:#222}.ico.blue{background:var(--blue)}.ico.red{background:var(--red)}
.contact-bar .sep{margin:0 12px}
.main-nav{position:absolute;top:66px;left:570px;display:flex;align-items:center;font-family:"Noto Serif",Georgia,serif;font-size:15px}
.main-nav a{color:var(--ink);text-decoration:none;padding:8px 14px}
.main-nav a.active{color:var(--red);border:2px solid var(--red);border-radius:20px;padding:6px 18px;font-weight:700}

/* hero */
.hero{position:absolute;left:0;top:120px;width:1200px;height:548px;background:linear-gradient(110deg,#5c6b3a 0%,#a79682 35%,#d7c8c0 55%,#6d7f4b 80%,#c9c7c3 100%)}
.hero-caption{position:absolute;left:100px;top:402px}
.hero-caption svg{display:block}
.hero-caption .txt{position:absolute;left:24px;top:18px;color:#fff;font-family:"Noto Serif",Georgia,serif;font-size:46px;line-height:56px;white-space:nowrap}
.hero-arrow{position:absolute;top:462px;width:52px;height:52px;border-radius:50%;display:flex;align-items:center;justify-content:center}
.hero-arrow.prev{left:974px;background:var(--red)}
.hero-arrow.next{left:1032px;background:var(--blue)}

/* intro */
.intro{position:absolute;left:98px;top:726px;width:462px}
.intro h2{font-family:"Noto Serif",Georgia,serif;font-weight:400;font-size:26px;color:var(--blue)}
.intro .lead{font-family:"Noto Serif",Georgia,serif;font-weight:700;font-size:13px;color:var(--red);margin-top:8px;white-space:nowrap}
.intro .sub{font-size:11px;line-height:22px;color:var(--ink);margin-top:4px}
.intro p{font-size:12px;line-height:22px;color:var(--muted)}
.intro .body{margin-top:10px}
.btn{display:inline-block;color:#fff;font-family:"Noto Serif",Georgia,serif;font-weight:700;font-size:14px;border-radius:2px;text-decoration:none}
.btn-red{background:var(--red)}
.btn-blue{background:var(--blue)}
.intro .btn{margin-top:14px;padding:7px 18px}
.video{position:absolute;left:566px;top:720px;width:532px;height:298px;background:radial-gradient(circle at 50% 40%,#2f6fd0,#0c2a6e 80%)}
.video .play{position:absolute;left:236px;top:112px;width:62px;height:62px;border-radius:50%;background:rgba(0,0,0,.55);display:flex;align-items:center;justify-content:center}

/* benefits */
.benefits{position:absolute;left:100px;top:1068px;width:998px;height:452px;background:linear-gradient(90deg,var(--red) 0%,#e2151d 45%,#7d2a2c 75%,#5a3a33 100%);color:#fff}
.benefits h2{position:absolute;left:66px;top:72px;font-family:"Noto Serif",Georgia,serif;font-size:26px;font-weight:700}
.benefits ul{position:absolute;left:66px;top:130px;list-style:none}
.benefits li{font-family:"Open Sans",Arial,sans-serif;font-weight:700;font-size:14.5px;line-height:31px;padding-left:28px;position:relative}
.benefits li::before{content:"";position:absolute;left:2px;top:14px;width:5px;height:5px;border-radius:50%;background:#fff}
.benefits .btn{position:absolute;left:64px;top:336px;padding:7px 14px}

/* services */
.services-title{position:absolute;left:0;top:1554px;width:1200px;text-align:center;font-family:"Noto Serif",Georgia,serif;font-weight:400;font-size:27px;line-height:33px;color:var(--blue)}
.service-card{position:absolute;top:1668px;width:306px;height:380px;background:#fff;box-shadow:0 3px 8px rgba(0,0,0,.22)}
.service-card .photo{height:254px}
.service-card h3{font-family:"Noto Serif",Georgia,serif;font-weight:400;font-size:26px;line-height:32px;text-align:center;margin-top:22px;color:var(--ink)}
.dots{position:absolute;top:2094px;left:535px;display:flex;gap:14px}
.dots span{width:14px;height:14px;border-radius:50%;background:#777}
.dots span.on{background:#fff;border:2px solid #777}

/* brochure */
.brochure{position:absolute;left:100px;top:2178px;width:998px;height:478px;background:linear-gradient(90deg,#254f8c,#3a6aa8 60%,#2f5e9c)}
.brochure .cover{position:absolute;left:40px;top:36px;width:304px;height:400px;background:linear-gradient(160deg,#aac3e6,#6f90b8 55%,#8a8f7a);box-shadow:0 4px 10px rgba(0,0,0,.35)}
.brochure h2{position:absolute;left:388px;top:46px;width:560px;text-align:center;color:#fff;font-family:"Noto Serif",Georgia,serif;font-weight:400;font-size:40px;line-height:52px}
.brochure p{position:absolute;left:386px;top:172px;width:560px;text-align:center;color:#fff;font-size:15px;line-height:30px}
.brochure .btn{position:absolute;left:550px;top:302px;height:50px;padding:0 22px;display:flex;align-items:center;gap:10px;font-family:"Open Sans",Arial,sans-serif;font-size:17px}

/* footer */
.site-footer h4{font-family:"Noto Serif",Georgia,serif;font-weight:400;font-size:21px;color:var(--ink)}
.quick-links{position:absolute;left:98px;top:2698px}
.quick-links ul{list-style:none;margin-top:18px}
.quick-links li{font-size:14px;line-height:31px;padding-left:38px;position:relative}
.quick-links li::before{content:"";position:absolute;left:2px;top:12px;width:8px;height:8px;border-radius:50%;background:#111}
.quick-links li.active{color:var(--red)}
.quick-links li.active::before{background:var(--red)}
.search{position:absolute;left:438px;top:2698px;width:330px}
.search .field{margin-top:22px;width:324px;height:34px;border:1px solid #bbb;box-shadow:inset 0 1px 3px rgba(0,0,0,.12);display:flex;align-items:center;justify-content:space-between;padding:0 14px;font-family:"Noto Serif",Georgia,serif;font-size:13px;color:#666}
.address{position:absolute;left:300px;top:2826px;width:600px;text-align:center;font-family:"Noto Serif",Georgia,serif;font-size:13px}
.call{position:absolute;left:300px;top:2856px;width:600px;text-align:center;font-family:"Noto Serif",Georgia,serif;font-size:24px;color:var(--red)}
.footer-brand{position:absolute;left:896px;top:2726px;display:flex;align-items:center;gap:8px;font-family:"Noto Serif",Georgia,serif;font-size:19px;color:var(--blue-dark)}
.footer-brand .brand-mark{width:20px;height:20px}
.social{position:absolute;left:908px;top:2788px;display:flex;gap:6px}
.social span{width:34px;height:34px;background:var(--blue)}
.social span:nth-child(4){background:var(--red)}
.social span:nth-child(5){background:#f07b22}
.copyright{position:absolute;left:0;top:2962px;width:1200px;text-align:center;font-size:12px}
</style>
</head>
<body>

<header class="site-header">
  <div class="brand"><span class="brand-mark"></span>Maplebrook Elders</div>
  <div class="contact-bar">
    <span class="ico dark"><svg width="16" height="12" viewBox="0 0 16 12"><rect x="1" y="1" width="14" height="10" fill="none" stroke="#fff" stroke-width="1.6"/><path d="M1 1l7 6 7-6" fill="none" stroke="#fff" stroke-width="1.6"/></svg></span>
    <span>info@maplebrookelders.example</span>
    <span class="ico blue" style="margin-left:22px"><svg width="14" height="14" viewBox="0 0 24 24"><path fill="#fff" d="M6.6 10.8a15.1 15.1 0 006.6 6.6l2.2-2.2a1 1 0 011-.25 11.4 11.4 0 003.6.57 1 1 0 011 1V20a1 1 0 01-1 1A17 17 0 013 4a1 1 0 011-1h3.5a1 1 0 011 1c0 1.25.2 2.45.57 3.57a1 1 0 01-.25 1z"/></svg></span>
    <span>Main: (555) 014-2290</span><span class="sep">|</span>
    <span class="ico red"><svg width="10" height="16" viewBox="0 0 10 16"><rect x="1" y="1" width="8" height="14" rx="1.5" fill="none" stroke="#fff" stroke-width="1.6"/><circle cx="5" cy="12.5" r="1" fill="#fff"/></svg></span>
    <span>Cell: (555) 014-7731</span>
  </div>
  <nav class="main-nav">
    <a class="active" href="#">Home</a><a href="#">Services</a><a href="#">About Us</a><a href="#">News</a><a href="#">Employment</a><a href="#">Contact us</a>
  </nav>
</header>

<section class="hero" role="img" aria-label="Photo of two smiling senior women sitting together on a porch">
  <div class="hero-caption">
    <svg width="626" height="176" viewBox="0 0 626 176"><polygon points="0,0 580,0 626,166 0,166" fill="rgba(0,0,0,.18)" transform="translate(0,10)"/><polygon points="0,0 578,0 622,168 0,168" fill="#2f6cb4"/></svg>
    <div class="txt">To Us<br>Its all about relationship</div>
  </div>
  <a class="hero-arrow prev" href="#" aria-label="Previous slide"><svg width="14" height="20" viewBox="0 0 14 20"><path d="M11 2L3 10l8 8" fill="none" stroke="#fff" stroke-width="2.5"/></svg></a>
  <a class="hero-arrow next" href="#" aria-label="Next slide"><svg width="14" height="20" viewBox="0 0 14 20"><path d="M3 2l8 8-8 8" fill="none" stroke="#fff" stroke-width="2.5"/></svg></a>
</section>

<section class="intro">
  <h2>Become a Junior Senior</h2>
  <div class="lead">Are you looking for a rewarding way to give back to the community?</div>
  <div class="sub">Would you like to support the greatest generation that ever lived while supplementing your income at the same time?</div>
  <p class="body">If you're a caring, loving and compassionate adult, aged 50 or older, and you can see yourself as a Junior Senior, we'd like to talk to you.</p>
  <p>Many Junior Seniors join Maplebrook Elders just before they retire or once they are fully retired. They come to us with decades of life experiences and a host of professional skills in nursing, teaching, business, social services, home management and government, to name just a few categories.</p>
  <a class="btn btn-red" href="#">Read more</a>
</section>
<a class="video" href="https://vidshare.example/Kq7PzLm2Wx4" role="img" aria-label="Promotional video for Maplebrook Elders">
  <span class="play"><svg width="22" height="26" viewBox="0 0 22 26"><polygon points="2,1 21,13 2,25" fill="#fff"/></svg></span>
</a>

<section class="benefits" role="img" aria-label="Photo of a caregiver and a senior man using a laptop together, under a red tint">
  <h2>There are many benefits to becoming a Junior Senior</h2>
  <ul>
    <li>Choose how many part time hours per week you would like to work (up to 29)</li>
    <li>Give back to your community</li>
    <li>Supplement your income</li>
    <li>Get paid for "volunteer" work</li>
    <li>Achieve fulfillment by helping others</li>
    <li>Add meaning to your life</li>
  </ul>
  <a class="btn btn-blue" href="#">Read more</a>
</section>

<h2 class="services-title">We are looking to fill positions that offer the following<br>non-medical in home care services:</h2>
<article class="service-card" style="left:100px">
  <div class="photo" role="img" aria-label="Photo of a caregiver helping a senior woman with a grocery basket" style="background:linear-gradient(135deg,#b9c9d6,#c8a98a 60%,#7e6a55)"></div>
  <h3>Grocery shopping</h3>
</article>
<article class="service-card" style="left:446px">
  <div class="photo" role="img" aria-label="Photo of two senior women talking at a table" style="background:linear-gradient(135deg,#e8e4dc,#c9c0d0 55%,#98b46a)"></div>
  <h3>Medical or dental<br>appointments</h3>
</article>
<article class="service-card" style="left:792px">
  <div class="photo" role="img" aria-label="Photo of a caregiver and a senior woman preparing a meal" style="background:linear-gradient(135deg,#8fa7b8,#d9b7a2 50%,#b2693f)"></div>
  <h3>Meal preparation &amp;<br>cleanup</h3>
</article>
<div class="dots"><span></span><span class="on"></span><span></span><span></span><span></span></div>

<section class="brochure">
  <div class="cover" role="img" aria-label="Brochure cover showing two senior women walking outdoors"></div>
  <h2>The careand company you<br>need to be at home</h2>
  <p>It's hard to admit that aging makes certain things more difficult, but asking for help doesn't mean giving up your independence. It means preserving it! Receiving assistance from someone who understands your position and how you want to live your life is the first step.</p>
  <a class="btn btn-red" href="#"><svg width="14" height="18" viewBox="0 0 14 18"><path d="M2 1h10v16l-5-4-5 4z" fill="none" stroke="#fff" stroke-width="1.8"/></svg>Download Brochure</a>
</section>

<footer class="site-footer">
  <div class="quick-links">
    <h4>Quick Links</h4>
    <ul><li class="active">Home</li><li>Services</li><li>About Us</li><li>News</li><li>Employment</li><li>Contact us</li></ul>
  </div>
  <div class="search">
    <h4>Search Maplebrook Elders</h4>
    <div class="field"><span>Search the site</span><svg width="14" height="14" viewBox="0 0 14 14"><circle cx="5.5" cy="5.5" r="4" fill="none" stroke="#111" stroke-width="2"/><path d="M8.5 8.5l4.5 4.5" stroke="#111" stroke-width="2.2"/></svg></div>
  </div>
  <div class="address">Address : P.O. Box 418, Alder Falls, New York 10990</div>
  <div class="call">Call : 555-014-2290 today!</div>
  <div class="footer-brand"><span class="brand-mark"></span>Maplebrook Elders</div>
  <div class="social" aria-label="Social links"><span></span><span></span><span></span><span></span><span></span></div>
  <div class="copyright">© 2017 | www.maplebrookelders.example</div>
</footer>

</body>
</html>
```